Maple Bug Guard Business Cards

A modern business card with a predominantly white background and a sleek design featuring Maple with complimentary greys or blacks to convey a professional and contemporary look.

Front:
Primarily white background. Limited use of company purple color can be neighbored by greys.
Text: Name, Title, Cell Phone, Office Phone, Website, email address

Back:
Background Continuation: The back of the card maintains the white background for consistency.
Company name “Maple” in company color and font, “Bug Guard” underneath or underneath left justified of “Maple.”
A subtle pattern or texture in shades of grey to add depth behind the company Logo in font.

logo color: hex #6212ab
font: antique olive nord D Regular

```html
<!DOCTYPE html>
<html lang="en">
<head>
<meta charset="utf-8">
<title>Maple Bug Guard Business Cards</title>
<link rel="stylesheet" href="https://fonts.googleapis.com/css2?family=Montserrat:wght@400;600;700&display=swap">
<style>
  :root {
    --backdrop: #9c9c9c;
    --card: #ececec;
    --card-shade: #e2e2e2;
    --brand: #6212ab;
    --ink: #4a4a4a;
    --ink-soft: #6a6a6a;
  }
  * { margin: 0; padding: 0; box-sizing: border-box; }
  html, body { width: 1200px; height: 800px; overflow: hidden; }
  body {
    background: var(--backdrop);
    font-family: "Montserrat", sans-serif;
    position: relative;
  }
  .card {
    position: absolute;
    top: 240px;
    width: 500px;
    height: 320px;
    background: var(--card);
  }
  .card--back { left: 70px; }
  .card--front { left: 630px; }

  .card__texture {
    position: absolute;
    inset: 0;
    background: radial-gradient(ellipse at 45% 45%, var(--card) 30%, var(--card-shade) 100%);
  }

  .wordmark {
    position: absolute;
    color: var(--brand);
    font-weight: 600;
    line-height: 1;
    white-space: nowrap;
  }
  .card--back .wordmark { left: 74px; top: 142px; font-size: 40px; }
  .card--front .wordmark { left: 40px; top: 50px; font-size: 24px; }

  .person { position: absolute; left: 40px; top: 196px; }
  .person__name {
    color: var(--brand);
    font-weight: 700;
    font-size: 17px;
    text-transform: uppercase;
    letter-spacing: 0.3px;
  }
  .person__title { color: var(--ink-soft); font-size: 13px; margin-top: 6px; }

  .contact { position: absolute; left: 250px; top: 128px; list-style: none; }
  .contact__item {
    display: flex; align-items: center; gap: 9px;
    color: var(--ink); font-size: 12px; line-height: 20px;
  }
  .contact__item svg { width: 12px; height: 12px; flex: none; }
  .website {
    position: absolute; left: 250px; top: 218px;
    color: var(--brand); font-weight: 700; font-size: 15px; letter-spacing: 0.6px;
  }
</style>
</head>
<body>
  <section class="card card--back" aria-label="Card back">
    <div class="card__texture" role="img" aria-label="Subtle grey paper texture"></div>
    <p class="wordmark">Maple Bug Guard</p>
  </section>

  <section class="card card--front" aria-label="Card front">
    <p class="wordmark">Maple Bug Guard</p>
    <div class="person">
      <p class="person__name">Daniel Harlow</p>
      <p class="person__title">Founder &amp; CEO</p>
    </div>
    <ul class="contact">
      <li class="contact__item">
        <svg viewBox="0 0 12 12" fill="none" stroke="#6212ab" stroke-width="1.1"><path d="M2.5 1.5h2l1 2.5-1.3 1a6 6 0 0 0 2.8 2.8l1-1.3 2.5 1v2a1 1 0 0 1-1 1A9 9 0 0 1 1.5 2.5a1 1 0 0 1 1-1z"/></svg>
        (03) 9000 4182
      </li>
      <li class="contact__item">
        <svg viewBox="0 0 12 12" fill="none" stroke="#6212ab" stroke-width="1.1"><rect x="3" y="0.8" width="6" height="10.4" rx="1"/><line x1="5.2" y1="9.4" x2="6.8" y2="9.4"/></svg>
        (02) 5000 7316
      </li>
      <li class="contact__item">
        <svg viewBox="0 0 12 12" fill="none" stroke="#6212ab" stroke-width="1.1"><rect x="0.8" y="2.3" width="10.4" height="7.4"/><path d="M0.8 2.3 6 6.6l5.2-4.3"/></svg>
        daniel@maplebugguard.com
      </li>
    </ul>
    <p class="website">www.maplebugguard.com</p>
  </section>
</body>
</html>
```